Label for a bottle of Gin soon to launch in the UK.

We need a label for a gin called Halworth Gin. It is very important that the label does not infringe any copyrights of the football club so please avoid the colour blue or anything related to football or the club. The example bottle below shows the bottle that we will be using. The gin will be clear not pink, the use of gold on the label is encouraged.
Should not infringe on the brand shown in the example image.

Club

Sans Serif

• Here is a link to the bottle that the label must fit onto https://www.flaskcrate-depot.co.uk/Glass-bottles/Glass-bottles/700ml-glass-bottles/700ml-clear-glass-bottle-Marosa.html
• No use of blue or anything related to football or Halworth Football Club or Moorhawks. Avoid Red also. White, gold and black should be primary colours used

```html
<!DOCTYPE html>
<html lang="en">
<head>
<meta charset="utf-8">
<title>Halworth Gin – Label Designs</title>
<link rel="stylesheet" href="https://fonts.googleapis.com/css2?family=Montserrat:wght@500;700&family=Open+Sans:wght@400;700;800&display=swap">
<style>
  :root {
    --backdrop: #f4f4f4;
    --charcoal: #333333;
    --gold: #c8b420;
    --gold-deep: #a3921a;
    --white: #ffffff;
    --soft-white: #e6e6e6;
  }
  html, body {
    margin: 0;
    padding: 0;
    width: 1200px;
    height: 964px;
    overflow: hidden;
    background: var(--backdrop);
  }
  .label-sheet {
    display: block;
    width: 1200px;
    height: 964px;
  }
  .label-body { fill: var(--charcoal); }
  .gold-rule { fill: none; stroke: var(--gold); stroke-width: 2; }
  .ribbon-tail { fill: var(--gold-deep); }
  .ribbon-band { fill: var(--gold); }
  .ribbon-name {
    font-family: "Open Sans", sans-serif;
    font-weight: 800;
    font-size: 21px;
    fill: var(--charcoal);
    letter-spacing: 0.5px;
  }
  .gin-vertical {
    font-family: "Montserrat", sans-serif;
    font-weight: 500;
    font-size: 60px;
    fill: var(--white);
    letter-spacing: 4px;
  }
  .gin-word {
    font-family: "Montserrat", sans-serif;
    font-weight: 700;
    font-size: 84px;
  }
  .gin-halo { fill: var(--white); }
  .gin-ring { fill: var(--charcoal); }
  .gin-core { fill: var(--white); }
  .batch-line {
    font-family: "Open Sans", sans-serif;
    font-weight: 700;
    font-size: 9.5px;
    fill: var(--white);
    letter-spacing: 0.6px;
  }
  .volume-line {
    font-family: "Open Sans", sans-serif;
    font-weight: 400;
    font-size: 8.5px;
    fill: var(--soft-white);
    letter-spacing: 0.6px;
  }
  .year-digit {
    font-family: "Open Sans", sans-serif;
    font-weight: 400;
    font-size: 10px;
    fill: var(--soft-white);
  }
  .year-rule { stroke: var(--soft-white); stroke-width: 0.8; }
  .emblem-placeholder { fill: var(--gold); }
</style>
</head>
<body>
<svg class="label-sheet" viewBox="0 0 1200 964" xmlns="http://www.w3.org/2000/svg" xmlns:xlink="http://www.w3.org/1999/xlink">
  <defs>
    <text id="gin-glyphs" class="gin-word" x="0" y="40" text-anchor="middle" letter-spacing="2">GIN</text>
  </defs>

  <!-- Neck strip, tall label variant -->
  <g class="neck-strip">
    <rect class="label-body" x="310" y="106" width="44" height="129"/>
    <rect class="gold-rule" x="315" y="110" width="34" height="121" stroke-width="1.4"/>
  </g>

  <!-- Tall front label -->
  <g class="front-label-tall">
    <rect class="label-body" x="278" y="372" width="110" height="385"/>
    <rect class="gold-rule" x="290" y="384" width="86" height="361"/>

    <g class="name-ribbon" transform="rotate(-5 333 433)">
      <polygon class="ribbon-tail" points="237,424 262,424 262,456 237,456 246,440"/>
      <polygon class="ribbon-tail" points="402,424 427,424 418,440 427,456 402,456"/>
      <rect class="ribbon-band" x="250" y="416" width="166" height="34"/>
      <text class="ribbon-name" x="333" y="440" text-anchor="middle">HALWORTH</text>
    </g>

    <text class="gin-vertical" transform="translate(355 530) rotate(-90)" text-anchor="middle">GIN</text>

    <rect class="emblem-placeholder" role="img" aria-label="Small gold emblem mark" x="319" y="612" width="28" height="28" transform="rotate(45 333 626)"/>

    <text class="batch-line" x="333" y="670" text-anchor="middle">HANDMADE</text>
    <text class="batch-line" x="333" y="682" text-anchor="middle">IN SMALL</text>
    <text class="batch-line" x="333" y="694" text-anchor="middle">BATCHES</text>
    <text class="volume-line" x="333" y="711" text-anchor="middle">ALC 40%</text>
    <text class="volume-line" x="333" y="722" text-anchor="middle">VOL 750ML</text>
  </g>

  <!-- Neck strip, star label variant -->
  <g class="neck-strip">
    <rect class="label-body" x="838" y="106" width="44" height="129"/>
    <rect class="gold-rule" x="843" y="110" width="34" height="121" stroke-width="1.4"/>
  </g>

  <!-- Star front label -->
  <g class="front-label-star" transform="translate(859 540)">
    <polygon class="label-body" points="0,-150 43.9,-106 106,-106 106,-43.9 150,0 106,43.9 106,106 43.9,106 0,150 -43.9,106 -106,106 -106,43.9 -150,0 -106,-43.9 -106,-106 -43.9,-106"/>
    <polygon class="gold-rule" points="0,-135.8 39.8,-96 96,-96 96,-39.8 135.8,0 96,39.8 96,96 39.8,96 0,135.8 -39.8,96 -96,96 -96,39.8 -135.8,0 -96,-39.8 -96,-96 -39.8,-96"/>

    <g class="name-ribbon" transform="rotate(-4 0 -58)">
      <polygon class="ribbon-tail" points="-84,-68 -60,-68 -60,-38 -84,-38 -76,-53"/>
      <polygon class="ribbon-tail" points="60,-68 84,-68 76,-53 84,-38 60,-38"/>
      <rect class="ribbon-band" x="-72" y="-74" width="144" height="32"/>
      <text class="ribbon-name" x="0" y="-51" text-anchor="middle">HALWORTH</text>
    </g>

    <g class="gin-wordmark">
      <g class="gin-halo">
        <use xlink:href="#gin-glyphs" x="-4.5" y="0"/>
        <use xlink:href="#gin-glyphs" x="4.5" y="0"/>
        <use xlink:href="#gin-glyphs" x="0" y="-4.5"/>
        <use xlink:href="#gin-glyphs" x="0" y="4.5"/>
        <use xlink:href="#gin-glyphs" x="-3.2" y="-3.2"/>
        <use xlink:href="#gin-glyphs" x="3.2" y="-3.2"/>
        <use xlink:href="#gin-glyphs" x="-3.2" y="3.2"/>
        <use xlink:href="#gin-glyphs" x="3.2" y="3.2"/>
      </g>
      <g class="gin-ring">
        <use xlink:href="#gin-glyphs" x="-2" y="0"/>
        <use xlink:href="#gin-glyphs" x="2" y="0"/>
        <use xlink:href="#gin-glyphs" x="0" y="-2"/>
        <use xlink:href="#gin-glyphs" x="0" y="2"/>
        <use xlink:href="#gin-glyphs" x="-1.4" y="-1.4"/>
        <use xlink:href="#gin-glyphs" x="1.4" y="-1.4"/>
        <use xlink:href="#gin-glyphs" x="-1.4" y="1.4"/>
        <use xlink:href="#gin-glyphs" x="1.4" y="1.4"/>
      </g>
      <use class="gin-core" xlink:href="#gin-glyphs"/>
    </g>

    <g class="year-mark">
      <line class="year-rule" x1="-56" y1="51" x2="-38" y2="51"/>
      <text class="year-digit" x="-47" y="62" text-anchor="middle">20</text>
      <line class="year-rule" x1="-56" y1="66" x2="-38" y2="66"/>
      <line class="year-rule" x1="38" y1="51" x2="56" y2="51"/>
      <text class="year-digit" x="47" y="62" text-anchor="middle">17</text>
      <line class="year-rule" x1="38" y1="66" x2="56" y2="66"/>
    </g>

    <text class="volume-line" x="0" y="57" text-anchor="middle">HANDMADE IN</text>
    <text class="volume-line" x="0" y="67" text-anchor="middle">SMALL BATCHES</text>
    <text class="batch-line" x="0" y="82" text-anchor="middle">ALC 40%  VOL 750 ML</text>
  </g>
</svg>
</body>
</html>
```